Stonelynk Business Card Design

The Stonelynk Co is an aggregate (crushing) equipment dealer serving Western Canadian provinces. Stonelynk is a distributor of aggregate equipment for different manufacturers.

We are looking to change and update the existing business card which has been used since the existence of the company. A copy of existing card has been attached for reference. The Stonelynk Co logo we want to remain the same and we want the green color to remain the same.

We are wanting something new with a different look. A refreshing card to show a new modern and updated look. No longer wanting to have the manufacturers on the back of the card but something more like our logo on the back of the card with a statement like "Crushing Solutions"

ideas could be:
- card can be different colors on front and back
- front or reverse of the card could possibly be the green color with the logo in black

Target Market(s)

Owners of Aggregate/Crushing companies

Requirements
Must have
• - logo to remain same along with same font within logo
• - green color to remain same
Nice to have
• as noted above under project description
Should not have

```html
<!DOCTYPE html>
<html lang="en">
<head>
<meta charset="utf-8">
<title>Stonelynk Business Card</title>
<link href="https://fonts.googleapis.com/css2?family=Roboto:wght@400;500;700&display=swap" rel="stylesheet">
<style>
  :root {
    --brand-green: #858d0b;
    --ink: #231f20;
    --paper: #ffffff;
    --text-grey: #3a3a3a;
    --stage: #e9e8e3;
  }
  * { margin: 0; padding: 0; box-sizing: border-box; }
  html, body { width: 1200px; height: 911px; overflow: hidden; }
  body {
    background: var(--stage);
    font-family: "Roboto", Arial, sans-serif;
    position: relative;
  }
  .card {
    position: absolute;
    width: 500px;
    height: 286px;
    border-radius: 18px;
    overflow: hidden;
    box-shadow: 0 6px 18px rgba(0,0,0,0.18);
  }
  .card--front { left: 70px; top: 312px; background: var(--brand-green); }
  .card--back  { left: 630px; top: 312px; background: var(--brand-green); }

  .front-panel { position: absolute; inset: 0; }

  .person {
    position: absolute;
    right: 34px;
    top: 30px;
    text-align: right;
  }
  .person__name {
    color: var(--brand-green);
    font-weight: 700;
    font-size: 17px;
    letter-spacing: 0.2px;
  }
  .person__title {
    color: var(--text-grey);
    font-size: 12.5px;
    font-weight: 500;
    margin-top: 2px;
  }

  .contact {
    position: absolute;
    left: 30px;
    bottom: 26px;
    list-style: none;
    font-size: 12.5px;
    color: var(--text-grey);
    line-height: 17px;
  }
  .contact li { display: flex; align-items: center; gap: 7px; }
  .contact svg { width: 11px; height: 11px; flex: none; }
  .contact__address { margin-top: 3px; }

  .brand {
    position: absolute;
    left: 0; right: 0;
    top: 96px;
    display: flex;
    flex-direction: column;
    align-items: center;
  }
  .brand__name {
    display: flex;
    align-items: center;
    gap: 12px;
    color: var(--ink);
    font-weight: 700;
    font-size: 30px;
    letter-spacing: 0.5px;
    text-transform: uppercase;
  }
  .brand__dot {
    width: 22px; height: 22px;
    border-radius: 50%;
    background: var(--ink);
  }
  .brand__tagline {
    margin-top: 14px;
    color: var(--ink);
    font-size: 14px;
    font-weight: 500;
  }
</style>
</head>
<body>

<section class="card card--front" aria-label="Card front">
  <svg class="front-panel" viewBox="0 0 500 286" preserveAspectRatio="none" aria-hidden="true">
    <path fill="var(--paper)" d="M130,0 H500 V200 A190,190 0 0 1 380,286 H0 V96 A190,190 0 0 1 130,0 Z"/>
  </svg>

  <div class="person">
    <p class="person__name">DALE MORROW</p>
    <p class="person__title">CEO/FOUNDER</p>
  </div>

  <ul class="contact">
    <li>
      <svg viewBox="0 0 12 12"><path fill="var(--brand-green)" d="M2.5 1l2 2-1 1.3c.7 1.5 1.8 2.6 3.2 3.2L8 6.5l2 2-1.3 1.8C4.8 10 2 7.2 1.7 2.4z"/></svg>
      780.555.0142
    </li>
    <li>
      <svg viewBox="0 0 12 12"><rect x="3" y="0.8" width="6" height="10.4" rx="1" fill="none" stroke="var(--brand-green)" stroke-width="1.4"/></svg>
      780.555.0187
    </li>
    <li>
      <svg viewBox="0 0 12 12"><rect x="1" y="4" width="10" height="7" fill="var(--brand-green)"/><rect x="3" y="1" width="6" height="3" fill="var(--brand-green)"/></svg>
      780.555.0163
    </li>
    <li>
      <svg viewBox="0 0 12 12"><rect x="0.5" y="2" width="11" height="8" fill="var(--brand-green)"/><path d="M1 2.5l5 4 5-4" fill="none" stroke="#fff" stroke-width="1"/></svg>
      dale@stonelynk.com
    </li>
    <li>
      <svg viewBox="0 0 12 12"><circle cx="6" cy="6" r="5.5" fill="var(--brand-green)"/><path d="M0.5 6h11M6 0.5c-2.5 3-2.5 8 0 11M6 0.5c2.5 3 2.5 8 0 11" fill="none" stroke="#fff" stroke-width="0.8"/></svg>
      www.stonelynk.ca
    </li>
    <li class="contact__address">2210- 48B Street, Nisku, Alberta T9E 5K2</li>
  </ul>
</section>

<section class="card card--back" aria-label="Card back">
  <div class="brand">
    <p class="brand__name"><span class="brand__dot" aria-hidden="true"></span>The Stonelynk Co.</p>
    <p class="brand__tagline">Crushing Solutions</p>
  </div>
</section>

</body>
</html>
```